Gravaloop bottle design

We're a small company looking for someone to help with our bottle design. We provide a sauce that will boost the flavor of packaged ramen. We're looking for a label that will stand out. I'm attaching some of the labels we like and some that I've made.

```html
<!DOCTYPE html>
<html lang="en">
<head>
<meta charset="utf-8">
<title>Gravaloop Ramen Sauce Label</title>
<link rel="stylesheet" href="https://fonts.googleapis.com/css2?family=Bebas+Neue&display=swap">
<style>
  :root {
    --page-bg: #ffffff;
    --label-cream: #e5d991;
    --brand-orange: #ec6a0f;
    --badge-red: #c0391b;
    --badge-text: #fbe88a;
  }
  html, body {
    margin: 0;
    padding: 0;
    width: 1200px;
    height: 1200px;
    overflow: hidden;
    background: var(--page-bg);
  }
  .canvas {
    position: relative;
    width: 1200px;
    height: 1200px;
  }
  .label {
    position: absolute;
    left: 350px;
    top: 100px;
    width: 500px;
    height: 1000px;
  }
  .brand-name {
    font-family: "Bebas Neue", "Arial Narrow", sans-serif;
    font-size: 206px;
    fill: var(--brand-orange);
  }
  .badge-text {
    font-family: "Bebas Neue", "Arial Narrow", sans-serif;
    font-size: 56px;
    fill: var(--badge-text);
    letter-spacing: 1px;
  }
</style>
</head>
<body>
<main class="canvas">
  <svg class="label" viewBox="0 0 500 1000" xmlns="http://www.w3.org/2000/svg">
    <defs>
      <clipPath id="label-shape">
        <path d="M0,50 Q0,0 50,0 H450 Q500,0 500,50 V930
                 C500,975 480,1000 456,1000
                 C436,1000 431,940 415,940 C399,940 394,1000 373,1000
                 C353,1000 348,940 332,940 C316,940 311,1000 290,1000
                 C270,1000 265,940 249,940 C233,940 228,1000 207,1000
                 C187,1000 182,940 166,940 C150,940 145,1000 124,1000
                 C104,1000 99,940 83,940 C67,940 62,1000 41,1000
                 C15,1000 0,975 0,930 Z"/>
      </clipPath>
      <linearGradient id="fire-fade" x1="0" y1="0" x2="0" y2="1">
        <stop offset="0" stop-color="#e5d991" stop-opacity="0"/>
        <stop offset="0.18" stop-color="#e98a3a" stop-opacity="0.7"/>
        <stop offset="0.32" stop-color="#e4600f"/>
        <stop offset="0.6" stop-color="#ef7a14"/>
        <stop offset="0.85" stop-color="#f39a1c"/>
        <stop offset="1" stop-color="#e55a0b"/>
      </linearGradient>
      <radialGradient id="fire-glow" cx="0.72" cy="0.72" r="0.45">
        <stop offset="0" stop-color="#fcd93a"/>
        <stop offset="1" stop-color="#fcd93a" stop-opacity="0"/>
      </radialGradient>
      <radialGradient id="fire-shadow" cx="0.2" cy="0.55" r="0.35">
        <stop offset="0" stop-color="#a8341a" stop-opacity="0.7"/>
        <stop offset="1" stop-color="#a8341a" stop-opacity="0"/>
      </radialGradient>
      <linearGradient id="noodle-tone" x1="0" y1="0" x2="0" y2="1">
        <stop offset="0" stop-color="#f3dfb2"/>
        <stop offset="1" stop-color="#e9c98d"/>
      </linearGradient>
    </defs>

    <g clip-path="url(#label-shape)">
      <rect class="label-bg" width="500" height="1000" fill="var(--label-cream)"/>

      <g class="hero-image" role="img" aria-label="Blurred fiery orange sauce background with chopsticks lifting a bundle of ramen noodles">
        <rect x="0" y="380" width="500" height="620" fill="url(#fire-fade)"/>
        <rect x="0" y="380" width="500" height="620" fill="url(#fire-shadow)"/>
        <rect x="0" y="380" width="500" height="620" fill="url(#fire-glow)"/>
        <ellipse cx="245" cy="790" rx="90" ry="190" fill="url(#noodle-tone)" opacity="0.55"/>
      </g>

      <g class="brand-name-block">
        <text class="brand-name" x="250" y="232" text-anchor="middle" textLength="404" lengthAdjust="spacingAndGlyphs">GRAVA</text>
        <text class="brand-name" x="250" y="388" text-anchor="middle" textLength="304" lengthAdjust="spacingAndGlyphs">LOOP</text>
      </g>

      <g class="product-badge">
        <rect x="102" y="524" width="296" height="67" fill="var(--badge-red)"/>
        <text class="badge-text" x="250" y="577" text-anchor="middle">RAMEN SAUCE</text>
      </g>
    </g>
  </svg>
</main>
</body>
</html>
```